New therapy private practice needs a 2 sided postcard announcing location and services

We need a postcard sized card that is TWO SIDED and shares our new location and services offered. (new location is 3840. W. 58th #2200 in Tulsa, OK 74129) Name of the therapy business is "Calm Harbor Counseling". Services offered include individual, marriage, family and group counseling. My phone number to place on the card is (918) 555-0148 and someone can call to schedule a free 20 minute consultation at that number.

These cards will also be mailed in an enclosed envelope or placed in welcome baskets as a marketing tool with possible referral sources like churches, doctors, and lawyers. (That means there does not have to be a space for an address or stamp to mail to. Full use of both sides of the card is important) We would like to see designs that use softer colors such as blue, purples, or greens. The final design should communicate a feeling of peace and hope and a sense of freshness and approachability. Incorporating a tag line such as..... "where you'll find hope!" would be good. My website is www.calmharborcare.example and extra info about my practice is on there. It is important my credentials are listed on the postcard. Dana Ruth Pell, LPC-S, LMFT

I am not looking for a bunch of "box looking pictures". The pictures I am uploading are for ideas, although my logo and picture should be used. I like the type of picture I have on my homepage of my website with the quote "Let your hopes, not your fears shape your future"

Target Market(s)

Primarily women and couples looking for counseling for relationships, anxiety, depression, or life transitions.

Font styles to use
Serif
Script

Colors
3276b5
85acd3
86cfc6
33b8a4
cadf82
876aae
9bcb3c

Requirements
Must have
• My picture, address, website, and phone number as well as my logo.
• Address is: 3840 W. 58th Street #2200 Tulsa, OK 74129
• Web: www.calmharborcare.example
• Email: dana@calmharborcare.example
• Phone: (918) 555-0148
• "Hope anchors the soul" - Heb. 6:19
• On my website, I have a 2 minute video of myself. This may be helpful to watch in getting a "feel" for my counseling practice.
• Services Provided: ANXIETY | DEPRESSION | LIFE TRANSITIONS | MARRIAGE COUNSELING | SEPARATION AND DIVORCE | WOMEN’S ISSUES | ADDICTIONS AND INFIDELITY | PARENT/CHILD RELATIONSHIPS | FAMILY CONFLICT | TRAUMA/GRIEF AND LOSS
Nice to have
• A combination of print and script would be nice. A feeling of tranquility and hope
• I would like to have the statement at the bottom of the card.... " It is my desire for you to discover that no matter the situation you are currently going through….. there’s hope!"
• It would also be nice to have a small area that says: Dana is a graduate of Western Lakeview College and has been in private practice for 11 years. She is a regular monthly co-host on the Meadow Broadcast Group at 88.3 FM
Should not have
• Heavy bold or abrasive feel

```html
<!DOCTYPE html>
<html lang="en">
<head>
<meta charset="utf-8">
<title>Calm Harbor Counseling – Postcard</title>
<link rel="stylesheet" href="https://fonts.googleapis.com/css2?family=Oswald:wght@400;500&family=Montserrat:wght@400;600&family=Great+Vibes&family=Allura&display=swap">
<style>
  :root {
    --page: #dcdcdc;
    --card-white: #ffffff;
    --sage: #88c39c;
    --forest: #3c7a4e;
    --leaf: #4b8a1e;
    --ink: #1d1d1d;
    --body-text: #2f3a33;
    --mist: #e6e6e6;
    --bar-gray: #cfcfcf;
    --accent-green: #5aa35e;
  }
  * { box-sizing: border-box; margin: 0; padding: 0; }
  html, body { width: 686px; height: 1200px; overflow: hidden; }
  body { background: var(--page); font-family: "Montserrat", sans-serif; color: var(--ink); position: relative; }

  .postcard {
    position: absolute; left: 23px; width: 640px; height: 488px;
    background: var(--card-white); overflow: hidden;
    box-shadow: 0 4px 10px rgba(0,0,0,.28);
  }
  .postcard--front { top: 88px; }
  .postcard--back { top: 624px; background: var(--mist); }

  .brand-bar { position: absolute; left: 0; bottom: 0; width: 100%; height: 9px; background: var(--leaf); }

  /* Front */
  .hero-photo {
    position: absolute; left: 0; top: 0; width: 389px; height: 443px;
    background: linear-gradient(180deg, #f4f1ec 0%, #e7e2d9 45%, #b9b3a6 72%, #8a7c68 100%);
  }
  .wordmark {
    position: absolute; display: flex; align-items: center; gap: 8px;
    font-family: "Montserrat", sans-serif; font-weight: 600; color: var(--forest);
  }
  .wordmark__dot { border-radius: 50%; background: var(--forest); flex: none; }
  .front-wordmark { left: 96px; top: 52px; font-size: 17px; }
  .front-wordmark .wordmark__dot { width: 26px; height: 26px; }

  .tagline-panel { position: absolute; left: 389px; top: 0; width: 251px; height: 443px; background: var(--sage); }
  .tagline-top {
    position: absolute; left: 0; width: 100%; top: 92px; text-align: center;
    font-family: "Oswald", sans-serif; font-weight: 500; font-size: 46px; letter-spacing: -.5px; color: var(--ink);
  }
  .tagline-script {
    position: absolute; left: 0; width: 100%; top: 130px; text-align: center;
    font-family: "Great Vibes", cursive; font-size: 88px; color: #fff; line-height: 1;
  }
  .tagline-band {
    position: absolute; left: 0; top: 228px; width: 100%; height: 103px; background: var(--forest);
    color: #fff; text-align: center; font-family: "Oswald", sans-serif; line-height: 1.05;
    padding-top: 20px;
  }
  .tagline-band__soft { display: block; font-weight: 400; font-size: 31px; }
  .tagline-band__strong { display: block; font-weight: 500; font-size: 33px; }

  .contact-strip {
    position: absolute; left: 0; top: 443px; width: 100%; height: 36px;
    display: flex; align-items: center; justify-content: center; gap: 22px;
    font-size: 13px; color: var(--ink);
  }
  .contact-item { display: flex; align-items: center; gap: 8px; }
  .contact-item svg { width: 17px; height: 17px; flex: none; }

  /* Back */
  .intro-panel { position: absolute; left: 0; top: 0; width: 100%; height: 224px; background: var(--sage); }
  .intro-copy { position: absolute; left: 32px; top: 18px; width: 330px; color: var(--body-text); }
  .intro-script { font-family: "Allura", cursive; font-size: 19px; color: var(--ink); margin-bottom: 8px; }
  .intro-text { font-size: 10px; line-height: 1.32; }
  .services-heading { font-size: 14px; font-weight: 600; color: var(--ink); margin: 10px 0 5px; }
  .services-list { font-size: 9.6px; line-height: 1.36; }
  .portrait {
    position: absolute; left: 377px; top: 6px; width: 210px; height: 218px;
    background: linear-gradient(180deg, #88c39c 0%, #d9c2a6 35%, #6b2a3a 80%, #2a2530 100%);
  }

  .location { position: absolute; left: 0; width: 100%; text-align: center; }
  .location-heading { top: 232px; font-family: "Allura", cursive; font-size: 23px; color: var(--ink); }
  .location-address {
    top: 268px; font-size: 13px; color: var(--body-text);
    display: flex; justify-content: center; align-items: center; gap: 8px;
  }
  .location-address svg { width: 14px; height: 17px; }
  .call-line { top: 308px; font-size: 14px; color: var(--body-text); }
  .call-line strong { font-weight: 600; font-size: 12.5px; }
  .call-line span { font-size: 12.5px; }
  .phone { top: 328px; font-size: 24px; font-weight: 600; color: var(--accent-green); letter-spacing: .5px; }

  .contact-bar {
    position: absolute; left: 113px; top: 367px; width: 423px; height: 23px; background: var(--bar-gray);
    display: flex; align-items: center; justify-content: center; gap: 20px; font-size: 11px; color: var(--body-text);
  }
  .contact-bar svg { width: 14px; height: 14px; }

  .closing-note { position: absolute; left: 32px; top: 432px; font-size: 10.5px; font-weight: 600; line-height: 1.35; color: var(--ink); }
  .back-wordmark { left: 440px; top: 424px; font-size: 13px; }
  .back-wordmark .wordmark__dot { width: 18px; height: 18px; }
  .credentials { position: absolute; right: 30px; top: 456px; font-size: 8px; color: #fff; }
</style>
</head>
<body>

<section class="postcard postcard--front" aria-label="Postcard front">
  <div class="hero-photo" role="img" aria-label="Photo: a woman with open arms facing the sea on a rocky beach"></div>
  <div class="wordmark front-wordmark"><span class="wordmark__dot"></span>Calm Harbor Counseling</div>

  <div class="tagline-panel">
    <div class="tagline-top">WOULD BE</div>
    <div class="tagline-script">Good</div>
    <div class="tagline-band">
      <span class="tagline-band__soft">Where You'll</span>
      <span class="tagline-band__strong">FIND HOPE!</span>
    </div>
  </div>

  <div class="contact-strip">
    <div class="contact-item">
      <svg viewBox="0 0 20 20"><path d="M2 8 L10 2 L18 8 V18 H2 Z" fill="none" stroke="#3c7a4e" stroke-width="2"/><path d="M2 8 L10 13 L18 8" fill="none" stroke="#3c7a4e" stroke-width="2"/></svg>
      dana@calmharborcare.example
    </div>
    <div class="contact-item">
      <svg viewBox="0 0 20 20"><circle cx="10" cy="10" r="8" fill="none" stroke="#5aa35e" stroke-width="2"/><path d="M2 10 H18 M10 2 C6 6 6 14 10 18 M10 2 C14 6 14 14 10 18" fill="none" stroke="#5aa35e" stroke-width="1.5"/></svg>
      www.calmharborcare.example
    </div>
  </div>
  <div class="brand-bar"></div>
</section>

<section class="postcard postcard--back" aria-label="Postcard back">
  <div class="intro-panel">
    <div class="intro-copy">
      <p class="intro-script">To finding your sense of</p>
      <p class="intro-text">Everyone goes through challenges in life, and while you may have successfully navigated through other difficulties, seeking out the help of a professional can be one of the healthiest decisions you make.</p>
      <p class="services-heading">Issues served</p>
      <p class="services-list">Anxiety | depression | life transitions | marriage counseling | separation and divorce | women's issues | addictions and infidelity | parent /child relationships | family conflict | trauma/grief and loss</p>
    </div>
    <div class="portrait" role="img" aria-label="Portrait photo of the counselor"></div>
  </div>

  <p class="location location-heading">New Location</p>
  <p class="location location-address">
    <svg viewBox="0 0 14 18"><path d="M7 1 C3.5 1 1 3.6 1 6.8 C1 11 7 17 7 17 C7 17 13 11 13 6.8 C13 3.6 10.5 1 7 1 Z" fill="none" stroke="#5aa35e" stroke-width="1.8"/><circle cx="7" cy="7" r="2.2" fill="#5aa35e"/></svg>
    3840 W. 58th Street #2200 Tulsa, OK 74129
  </p>
  <p class="location call-line">Call Now to Schedule a <strong>FREE 20 minute</strong> <span>consultation</span></p>
  <p class="location phone">(918) 555-0148</p>

  <div class="contact-bar">
    <div class="contact-item">
      <svg viewBox="0 0 20 20"><path d="M2 8 L10 2 L18 8 V18 H2 Z" fill="none" stroke="#3c7a4e" stroke-width="2"/><path d="M2 8 L10 13 L18 8" fill="none" stroke="#3c7a4e" stroke-width="2"/></svg>
      dana@calmharborcare.example
    </div>
    <div class="contact-item">
      <svg viewBox="0 0 20 20"><circle cx="10" cy="10" r="8" fill="none" stroke="#5aa35e" stroke-width="2"/><path d="M2 10 H18 M10 2 C6 6 6 14 10 18 M10 2 C14 6 14 14 10 18" fill="none" stroke="#5aa35e" stroke-width="1.5"/></svg>
      www.calmharborcare.example
    </div>
  </div>

  <p class="closing-note">It is my desire for you to discover that no matter<br>the situation you are currently going through</p>
  <div class="wordmark back-wordmark"><span class="wordmark__dot"></span>Calm Harbor Counseling</div>
  <p class="credentials">Dana Ruth Pell, LPC-S, LMFT</p>
  <div class="brand-bar"></div>
</section>

</body>
</html>
```